Web Design & Programming for Health & Wellness Coaching Company (PageFoundry or Scribeloom)

Business Info: I'm starting a health coaching business (Colette Marsh, PhD, Health & Wellness Coaching @ colettemarshwell.com) and need some help designing my website (colettemarshwell.com).

Basics: I have the domain purchased on pagefoundry.com that is also linked to Scribeloom (so designer/programmer can program into pagefoundry.com or Scribeloom.com). I want my primary color to be aqua blue (see 1st photo/pdf attached) and my secondary colors to be spring green (1) and deep purple/magenta (see 2nd photo/pdf attached as well as the last photo attached).

There will be 5 pages: 1) Home; 2) Services; 3) Coaching Philosophy; 4) About Me; 5) Blog; 6) Client Resources; 7) Contact Me

I want there to be a banner at the top of each page, on the right-hand side (align right) that has links to all other pages, as well as a “book a consult” icon (that links to an appointment book where clients can see my schedule and book an appointment) and a cart icon, where clients can check out and pay. The cart will need to be linked to a pay service. The banner should roughly appear as follows:
Home | Services | Coaching Philosophy | About Me | [Book a Consult Icon] | [Cart Icon]

I also want there to be a small, centered area for hyperlinks at the bottom of each page that appears as follows (with everything hyperlinked):

Home | Services | Coaching Philosophy | About Me
555-314-2786 | colette@colettemarshwell.com
Colette Marsh, PhD, LLC | © 2022

“Home Page:” I would like my home page to have 3-4 main aspects: 1) a marquis of photos of me (included below; one main photo, but with options for clients to right/left click to scroll through several photos); 2-3) space for text about my coaching philosophy and program 3) a marquis of client testimonials that clients can scroll through. I like the setup of this homepage: https://www.tidewellcoach.example but using my color scheme (below). I want the home page to have the water background shown in the first image (but not the surfers).

“Services page:” I offer the following 5 services: 1) Free Health History Consultation; 2) Standard 6-Month Program; 3) Deluxe 6-Month Program; 4) Coastal Calm Insight Card Reading; 5) Customized Options.

I want each service to be shown on the Services page and to contain a “Book Appointment” or “Purchase” button/link (Services #1-2 should have the “Book appointment” button and services #3-5 should have the “Purchase” button). I want the “Book appointment” button to link to a calendar where clients can see my schedule and book an appointment. Both links should also cause the item to appear in the cart, and the cart should be linked to a pay feature that can take clients’ credit card info, etc.

The “About Me” Page should say “About Me” then have 1 photo (with arrow options on both sides so clients can scroll through different photos). Below the photo should be a block of text where I can include a few paragraphs about me. Below the text should be links to the following pages, which can appear as follows:

Find Me on Social Media:
Current: https://olvera-institute.example/profile/cmarsh
ConnectWork: https://www.connectworknet.example/in/colette-marsh-52718406/
FriendSpace: https://www.friendspace.example/colette.marsh
SnapGallery: https://www.snapgallery.example/colettem_hikes/?hl=en

The “Coaching Philosophy” page should be similar to the “About Me” page (minus the “Follow Me on social media” part). This page should have 2 icon/links below the text: 1 that says “Let’s Get Started” and directs patients to my calendar where they can book a free 1hr health coaching consultation; 1 that says “Book a Service” and takes clients to the services page.

The “Blog” page will be a standard blog page.

The “Client Resources” page will be for client resources. I would like for this page to require clients to enter their a login name and password (provided by me).

More about my business:
My health coaching certification is through the Academy of Holistic Dietetics (AHD, holisticdieteticsacademy.com). I also have a PhD in Basic Biomedical Science & Neuroscience (specializing in addiction) and post-doctorate experience at the Olvera Institute of Botanical Healing in alternative/complementary and integrative health interventions for binge eating and obesity (things like 12-step interventions, yoga, acupuncture, meditation, herbs, etc.).

My health coaching practice centers around 2 concepts: 1) the client can heal his/herself by him/herself; I am simply here to help the client tap into his/her own healing intuition; 2) I believe in wholistic healing that brings primary and secondary foods into balance. Secondary foods are the foods we put on our plate and eat. Primary foods are everything else in our life that nourishes us (e.g., creativity, relationships, movement, joy, finances, etc.). When the secondary foods are a problem, it's usually a sign that our primary foods are imbalanced, so I help clients identify how to rebalance both.

I also included some sample photos that will on the "about me" page of my website. I focus on connection, movement, and nature, so lots of nature themes. Mountains.

Here are some other relevant "about me" websites:

Target Market(s)

Adult females and males who live busy lives and want help and support in creating transformation and breakthroughs, on their plates (nutrition) and in their lives.

Industry/Entity Type

Health and Wellness

Number of Pages Required

5+ page

Font styles to use
Serif
Sans Serif

Colors
0094D4
00A9DD
6FCCEA
C7EBF8
E9F6FB

Requirements
Must have
• See project description
Nice to have
• See project description

```html
<!DOCTYPE html>
<html lang="en">
<head>
<meta charset="utf-8">
<title>Colette Marsh — Health Coaching &amp; Philosophy</title>
<link href="https://fonts.googleapis.com/css2?family=Cinzel:wght@400&family=Mulish:ital,wght@0,400;0,700;0,800;1,400&display=swap" rel="stylesheet">
<style>
:root{
  --aqua:#00A9DD;
  --aqua-deep:#0094D4;
  --aqua-soft:#6FCCEA;
  --aqua-pale:#C7EBF8;
  --aqua-mist:#E9F6FB;
  --ink:#1c3a48;
  --text:#3a4a52;
  --white:#ffffff;
  --arrow-grey:#c9cdd1;
}
*{box-sizing:border-box;margin:0;padding:0}
html,body{width:1200px;height:3066px;overflow:hidden;background:var(--white)}
body{font-family:"Mulish",Arial,sans-serif;color:var(--text)}
.canvas{position:relative;width:1200px;height:3066px;overflow:hidden;background:var(--white)}
.abs{position:absolute}
.serif{font-family:"Cinzel",Georgia,serif;font-weight:400}

/* header */
.site-logo{left:90px;top:22px;font-family:"Cinzel",Georgia,serif;font-size:29px;color:var(--aqua-soft);letter-spacing:.5px}
.main-nav a{position:absolute;top:31px;font-size:13px;color:#222;text-decoration:none;letter-spacing:.2px}
.consult-btn{left:781px;top:19px;width:178px;height:39px;border-radius:20px;background:var(--aqua);color:var(--white);font-size:13px;font-weight:700;display:flex;align-items:center;justify-content:center;gap:8px;letter-spacing:.2px}
.cart{left:1004px;top:28px}

/* hero */
.hero-photo{left:0;top:95px;width:1200px;height:630px;background:linear-gradient(180deg,#f4f8fb 0%,#cfdfe8 18%,#5d7f86 36%,#2f5239 52%,#6f7a3e 66%,#b99b55 80%,#a58a55 100%)}
.hero-title{left:0;width:1200px;top:148px;text-align:center;font-size:60px;color:var(--ink);letter-spacing:1px}
.hero-sub{left:0;width:1200px;top:220px;text-align:center;font-size:35px;color:var(--ink);letter-spacing:.5px}
.hero-wave{left:0;top:600px}

/* section backdrops */
.backdrop-lake{left:0;top:1080px;width:1200px;height:260px;background:linear-gradient(180deg,rgba(255,255,255,0) 0%,#b9d4e4 35%,#d9ebf3 60%,#ffffff 100%)}
.backdrop-coast{left:0;top:1830px;width:1200px;height:520px;background:linear-gradient(180deg,#ffffff 0%,#e2edf2 30%,#c4d6de 55%,#dde8ec 75%,#ffffff 100%)}
.backdrop-shore{left:0;top:2580px;width:1200px;height:255px;background:linear-gradient(180deg,#ffffff 0%,#b8d2e3 35%,#cfe3ee 65%,#e9f3f8 100%)}

/* bio */
.photo-frame{position:absolute;background:linear-gradient(160deg,#6f8799,#b59470 55%,#e8e2d6)}
.photo-frame::after{content:"";position:absolute;left:11px;top:11px;right:11px;bottom:11px;border:3px solid var(--white)}
.slider-arrow{position:absolute}
.bio-name{left:634px;top:836px;font-size:42px;color:var(--aqua-deep)}
.bio-role{left:634px;top:884px;font-size:29px;color:var(--aqua-deep)}
.underline{position:absolute;height:4px;border-radius:50%;background:var(--aqua-deep)}
.body-copy{font-size:16.5px;line-height:28px;color:var(--text)}
.bio-copy{left:639px;top:951px;width:500px}
.bio-copy p + p{margin-top:3px}
.outline-btn{left:641px;top:1151px;width:174px;height:50px;border:2px solid var(--aqua-deep);color:var(--aqua-deep);font-size:16px;display:flex;align-items:center;justify-content:center;background:rgba(255,255,255,.6)}

/* philosophy */
.section-title{font-size:44px;color:var(--aqua-deep);letter-spacing:.5px}
.philo-title{left:0;width:1200px;top:1342px;text-align:center}
.philo-intro{left:200px;width:800px;top:1427px;text-align:center}
.benefit-icon{position:absolute;width:94px;height:94px;border-radius:50%;border:2px solid var(--aqua);display:flex;align-items:center;justify-content:center}
.benefit-icon span{width:82px;height:82px;border-radius:50%;background:var(--aqua);display:flex;align-items:center;justify-content:center}
.benefit-text{position:absolute;font-size:17.5px;line-height:27px;color:#2a2f33}

/* program */
.program-title{left:130px;top:1937px}
.program-copy{left:130px;top:2029px;width:500px}
.program-copy p + p{margin-top:34px}

/* testimonials */
.testi-title{left:0;width:1220px;top:2397px;text-align:center}
.testi-card{left:304px;top:2525px;width:586px;height:220px;border:2px solid var(--aqua-deep);background:rgba(255,255,255,.55)}
.testi-avatar{left:556px;top:2483px;width:76px;height:76px;border-radius:50%;background:radial-gradient(circle at 50% 40%,#6a4a3a,#2b2a2f 60%,#3e8fc4 100%)}
.testi-quote{left:344px;width:510px;top:2581px;text-align:center;font-style:italic;font-size:18px;line-height:27px;color:#4a5257}
.testi-name{left:304px;width:586px;top:2680px;text-align:center;font-size:18px;color:#333}

/* footer */
.site-footer{left:0;top:2835px;width:1200px;height:231px;background:linear-gradient(180deg,#00b9e2 0%,#00c5de 100%);color:var(--white);text-align:center}
.footer-nav{position:absolute;top:66px;left:0;width:1200px;display:flex;justify-content:center;gap:46px;font-size:16.5px;font-weight:800;letter-spacing:.3px}
.footer-contact{position:absolute;top:98px;left:0;width:1200px;font-size:15px}
.footer-legal{position:absolute;top:130px;left:0;width:1200px;font-size:13.5px}
.footer-social{position:absolute;top:165px;left:0;width:1200px;display:flex;justify-content:center;gap:8px}
.footer-social span{width:27px;height:27px;border-radius:50%;background:var(--white)}
</style>
</head>
<body>
<div class="canvas">

  <!-- header -->
  <div class="abs site-logo">COLETTEMARSH</div>
  <nav class="main-nav">
    <a style="left:328px">HOME</a>
    <a style="left:400px">SERVICES</a>
    <a style="left:492px">COACHING PHILOSOPHY</a>
    <a style="left:678px">ABOUT ME</a>
  </nav>
  <div class="abs consult-btn">
    <svg width="18" height="18" viewBox="0 0 18 18" fill="none" stroke="#fff" stroke-width="1.6"><rect x="2" y="3.5" width="14" height="12.5" rx="1"/><path d="M2 7.5h14M6 1.5v4M12 1.5v4M5 10.5h2M8.5 10.5h2M12 10.5h1.5M5 13h2M8.5 13h2"/></svg>
    BOOK A CONSULT
  </div>
  <svg class="abs cart" width="22" height="20" viewBox="0 0 22 20" fill="none" stroke="#1a87b8" stroke-width="1.6"><path d="M1 2h3l2.5 10h11l2-7H5.2"/><circle cx="8" cy="16.5" r="1.6"/><circle cx="16" cy="16.5" r="1.6"/></svg>

  <!-- hero -->
  <div class="abs hero-photo" role="img" aria-label="Photo of a runner on a grassy mountain trail among pine trees under a misty sky"></div>
  <div class="abs hero-title serif">WELCOME TO COLETTEMARSH</div>
  <div class="abs hero-sub serif">HEALTH COACHING &amp; PHILOSOPHY</div>
  <svg class="abs hero-wave" width="1200" height="140" viewBox="0 0 1200 140">
    <path d="M0 30 C200 120 420 110 620 70 C820 30 1000 40 1200 45 L1200 140 L0 140 Z" fill="#fff"/>
    <path d="M0 30 C150 110 380 125 600 80 C800 38 960 46 1080 48" fill="none" stroke="#00A9DD" stroke-width="7" stroke-linecap="round"/>
  </svg>

  <!-- backdrops -->
  <div class="abs backdrop-lake" role="img" aria-label="Soft photo of a calm lake with distant blue mountains"></div>
  <div class="abs backdrop-coast" role="img" aria-label="Faded photo of a rocky shoreline under a bright sky"></div>
  <div class="abs backdrop-shore" role="img" aria-label="Soft photo of calm water and pale blue hills"></div>

  <!-- bio -->
  <div class="photo-frame" style="left:158px;top:837px;width:382px;height:366px" role="img" aria-label="Portrait photo of the coach smiling outdoors"></div>
  <svg class="slider-arrow" style="left:126px;top:1006px" width="20" height="28" viewBox="0 0 20 28"><path d="M15 3 L5 14 L15 25" fill="none" stroke="#0094D4" stroke-width="4" stroke-linecap="round"/></svg>
  <svg class="slider-arrow" style="left:551px;top:1006px" width="20" height="28" viewBox="0 0 20 28"><path d="M5 3 L15 14 L5 25" fill="none" stroke="#0094D4" stroke-width="4" stroke-linecap="round"/></svg>
  <div class="abs bio-name serif">COLETTE MARSH, PHD,</div>
  <div class="abs bio-role serif">HEALTH &amp; WELLNESS COACHING</div>
  <div class="underline" style="left:634px;top:915px;width:107px"></div>
  <div class="abs body-copy bio-copy">
    <p>Lorem ipsum dolor sit amet, consectetur adipiscing elit, sed do eiusmod tempor incididunt ut labore et dolore magna aliqua.</p>
    <p>Ut enim ad minim veniam, quis nostrud exercitation ullamco laboris nisi ut aliquip ex ea commodo consequat. Duis aute irure dolor in reprehenderit in voluptate velit esse cillum dolore eu fugiat nulla pariatur. Excepteur sint occaecat cupidat</p>
  </div>
  <div class="abs outline-btn">LEARN MORE</div>

  <!-- philosophy -->
  <div class="abs section-title serif philo-title">COACHING PHILOSOPHY</div>
  <div class="underline" style="left:554px;top:1401px;width:108px"></div>
  <div class="abs body-copy philo-intro">Lorem ipsum dolor sit amet, consectetur adipiscing elit, sed do eiusmod tempor incididunt ut labore et dolore magna aliqua. Ut enim ad minim veniam, quis nostrud</div>

  <div class="benefit-icon" style="left:147px;top:1530px"><span>
    <svg width="44" height="44" viewBox="0 0 44 44" fill="none" stroke="#fff" stroke-width="1.6"><circle cx="22" cy="19" r="12"/><circle cx="22" cy="19" r="4"/><path d="M22 7v4M22 27v4M10 19h4M30 19h4M16 34h12M18 38h8"/></svg>
  </span></div>
  <div class="benefit-text" style="left:256px;top:1544px">Coaching results in new behaviors and<br>new skill development.</div>

  <div class="benefit-icon" style="left:628px;top:1538px"><span>
    <svg width="44" height="44" viewBox="0 0 44 44" fill="none" stroke="#fff" stroke-width="1.8"><rect x="6" y="28" width="5" height="9"/><rect x="15" y="24" width="5" height="13"/><rect x="24" y="20" width="5" height="17"/><rect x="33" y="14" width="5" height="23"/><path d="M6 22 L30 8 M25 7h6v6"/></svg>
  </span></div>
  <div class="benefit-text" style="left:736px;top:1544px">Coaching improves psychological<br>resources that predict higher performance,<br>capacity to change</div>

  <div class="benefit-icon" style="left:147px;top:1667px"><span>
    <svg width="44" height="44" viewBox="0 0 44 44" fill="none" stroke="#fff" stroke-width="1.6"><path d="M8 6h28" stroke-dasharray="2 2"/><circle cx="14" cy="18" r="6"/><path d="M12 24v4h4v-4M6 38v-6h16v6"/><circle cx="31" cy="17" r="4"/><path d="M31 10v2M31 22v2M24 17h2M36 17h2M22 38v-6h16v6"/></svg>
  </span></div>
  <div class="benefit-text" style="left:256px;top:1680px">Coaching is related to increased<br>positivity, resilience, and self-efficacy.</div>

  <div class="benefit-icon" style="left:628px;top:1674px"><span>
    <svg width="44" height="44" viewBox="0 0 44 44" fill="none" stroke="#fff" stroke-width="1.6"><circle cx="24" cy="15" r="9"/><path d="M20 15h8M24 11v8"/><path d="M5 30h8l6 3h10l8-5M5 37h20l12-6"/></svg>
  </span></div>
  <div class="benefit-text" style="left:736px;top:1687px">Coaching results in new behaviors and new<br>skill development.</div>

  <!-- program -->
  <div class="abs section-title serif program-title">ABOUT PROGRAM</div>
  <div class="underline" style="left:130px;top:1990px;width:107px"></div>
  <div class="abs body-copy program-copy">
    <p>Lorem ipsum dolor sit amet, consectetur adipiscing elit, sed do eiusmod tempor incididunt ut labore et dolore magna aliqua. Ut enim ad minim veniam, quis nostrud exercitation ullamco</p>
    <p>laboris nisi ut aliquip ex ea commodo consequat. Duis aute irure dolor in reprehenderit in voluptate velit esse cillum dolore eu fugiat nulla pariatur. Excepteur sint occaecat cupidat</p>
  </div>
  <div class="photo-frame" style="left:648px;top:1906px;width:442px;height:374px;background:linear-gradient(180deg,#c9d6e2 0%,#a7a7a0 30%,#2f4a31 55%,#243b26 80%,#b3b1a6 100%)" role="img" aria-label="Photo of a hiker in a pine forest beneath a snowy mountain peak"></div>

  <!-- testimonials -->
  <div class="abs section-title serif testi-title">CLIENT TESTIMONIALS</div>
  <div class="underline" style="left:564px;top:2446px;width:68px;height:3px;border-radius:2px"></div>
  <div class="abs testi-card"></div>
  <div class="abs testi-avatar" role="img" aria-label="Client portrait photo"></div>
  <div class="abs testi-quote">“Lorem ipsum dolor sit amet, consectetur adipiscing elit, sed do eiusmod tempor incididunt ut labore et dolore magna aliqua. Ut enim ad minim veniam quis nostrud “</div>
  <div class="abs testi-name">Nora Halvorsen</div>
  <svg class="slider-arrow" style="left:216px;top:2612px" width="26" height="40" viewBox="0 0 26 40"><path d="M21 3 L6 20 L21 37" fill="none" stroke="#c9cdd1" stroke-width="5" stroke-linecap="round"/></svg>
  <svg class="slider-arrow" style="left:973px;top:2612px" width="26" height="40" viewBox="0 0 26 40"><path d="M5 3 L20 20 L5 37" fill="none" stroke="#c9cdd1" stroke-width="5" stroke-linecap="round"/></svg>

  <!-- footer -->
  <footer class="abs site-footer">
    <div class="footer-nav"><span>HOME</span><span>SERVICES</span><span>COACHING PHILOSOPHY</span><span>ABOUT ME</span></div>
    <div class="footer-contact">555-314-2786 &nbsp;&nbsp; | &nbsp;&nbsp; colette@colettemarshwell.com</div>
    <div class="footer-legal">Colette Marsh, PhD, LLC | © 2022</div>
    <div class="footer-social"><span></span><span></span><span></span><span></span></div>
  </footer>
</div>
</body>
</html>
```